Corrigan & Hale, LLC
Business Cards & Stationery
Corrigan & Hale, LLC -
Creative Brief
Professional
Deborah L. Corrigan
Attorney At Law
418 W. Brookfield Avenue Suite 3B Pearl River, New York 10965-2274
dcorrigan@corriganandhale-example.com
www.corriganandhale-example.com
We will need to be able to use template for other people in the firm.
Specializing in Civil Litigation, Wills, Trusts & Estates, Guardianships, and related matters

```html
<!DOCTYPE html>
<html lang="en">
<head>
<meta charset="utf-8">
<title>Corrigan &amp; Hale, LLC — Business Card</title>
<link rel="stylesheet" href="https://fonts.googleapis.com/css2?family=Cinzel:wght@500&family=Crimson+Text:ital,wght@0,400;0,600;1,600&display=swap">
<style>
  :root {
    --backdrop: #e9e7e3;
    --card: #ffffff;
    --green: #1c6b3a;
    --green-deep: #0f4d27;
    --swoosh: #2e2e2e;
    --ink: #2b2b2b;
    --ink-soft: #4a4a4a;
    --rule: #9a9a9a;
  }
  * { margin: 0; padding: 0; box-sizing: border-box; }
  html, body { width: 1200px; height: 780px; overflow: hidden; background: var(--backdrop); }
  .card {
    position: absolute; left: 100px; top: 104px; width: 1000px; height: 572px;
    background: var(--card); border-radius: 28px; overflow: hidden;
    box-shadow: 0 10px 30px rgba(0,0,0,.18);
    font-family: "Crimson Text", Georgia, serif; color: var(--ink);
  }
  .card__band { position: absolute; left: 0; top: 0; width: 1000px; height: 572px; }
  .holder { position: absolute; right: 44px; top: 34px; text-align: right; color: #fff; font-style: italic; font-weight: 600; }
  .holder__name { font-size: 38px; line-height: 1.1; }
  .holder__title { font-size: 24px; line-height: 1.2; }
  .firm { position: absolute; left: 176px; top: 268px; display: flex; align-items: center; gap: 26px; }
  .firm__mark { width: 72px; height: 72px; background: var(--green); }
  .firm__name { font-family: "Cinzel", Georgia, serif; font-weight: 500; font-size: 44px; color: var(--ink); letter-spacing: .5px; }
  .firm__practice {
    position: absolute; left: 274px; top: 328px; width: 560px; padding-top: 8px;
    border-top: 1.5px solid var(--rule);
    font-size: 18px; letter-spacing: 3px; text-transform: uppercase; color: var(--ink-soft); text-align: right;
  }
  .address { position: absolute; right: 530px; top: 420px; text-align: right; font-size: 23px; line-height: 1.2; color: var(--ink); font-style: normal; }
  .divider { position: absolute; left: 488px; top: 392px; width: 1.5px; height: 120px; background: var(--rule); }
  .contacts { position: absolute; left: 510px; top: 392px; list-style: none; font-size: 21px; line-height: 30px; color: var(--ink); }
  .contacts li { display: flex; align-items: center; gap: 12px; }
  .contacts svg { width: 18px; height: 18px; flex: none; }
</style>
</head>
<body>
  <article class="card">
    <svg class="card__band" viewBox="0 0 1000 572" aria-hidden="true">
      <defs>
        <linearGradient id="bandGreen" x1="0" y1="0" x2="0" y2="1">
          <stop offset="0" stop-color="#1f7a42"/>
          <stop offset="1" stop-color="#14592f"/>
        </linearGradient>
      </defs>
      <path d="M0,0 H1000 V150 C780,150 560,200 330,228 C200,244 90,238 0,222 Z" fill="url(#bandGreen)"/>
      <path d="M0,222 C90,238 200,244 330,228 C560,200 780,150 1000,150 V160 C780,168 560,218 330,246 C200,262 90,258 0,240 Z" fill="var(--swoosh)"/>
    </svg>

    <header class="holder">
      <p class="holder__name">Deborah L. Corrigan</p>
      <p class="holder__title">Attorney At Law</p>
    </header>

    <div class="firm">
      <span class="firm__mark"></span>
      <span class="firm__name">Corrigan &amp; Hale, LLC</span>
    </div>
    <p class="firm__practice">Attorneys at Law</p>

    <address class="address">
      418 W. Brookfield Avenue<br>
      Suite 3B, Alder Falls<br>
      New York 10987-2274
    </address>

    <span class="divider"></span>

    <ul class="contacts">
      <li>
        <svg viewBox="0 0 18 18" aria-hidden="true"><path d="M4 1 L7 5 L5.5 7 C6.5 9.5 8.5 11.5 11 12.5 L13 11 L17 14 L15 17 C8 17 1 10 1 3 Z" fill="var(--green)"/></svg>
        212.555.0147
      </li>
      <li>
        <svg viewBox="0 0 18 18" aria-hidden="true"><rect x="4" y="1" width="10" height="5" fill="var(--green)"/><rect x="1" y="7" width="16" height="7" rx="1.5" fill="var(--green)"/><rect x="4" y="12" width="10" height="5" fill="var(--green-deep)"/></svg>
        212.555.0183
      </li>
      <li>
        <svg viewBox="0 0 18 18" aria-hidden="true"><text x="9" y="14.5" text-anchor="middle" font-size="17" font-weight="700" fill="var(--green)" font-family="Arial, sans-serif">@</text></svg>
        dcorrigan@corriganandhale-example.com
      </li>
      <li>
        <svg viewBox="0 0 18 18" aria-hidden="true"><circle cx="9" cy="9" r="7.5" fill="none" stroke="var(--green)" stroke-width="1.6"/><ellipse cx="9" cy="9" rx="3.2" ry="7.5" fill="none" stroke="var(--green)" stroke-width="1.3"/><path d="M1.5 9 H16.5" stroke="var(--green)" stroke-width="1.3"/></svg>
        www.corriganandhale-example.com
      </li>
    </ul>
  </article>
</body>
</html>
```